Brisk Tide Womens Shaving Foam (For sale in supermarkets).

We supply supermarkets with various products and now need a new design for a Ladies Shaving Foam Can. Soft Pink on the bottom of the can finishing of gradated into white. Needs to have a Shaving Foam swirl image also needs to have our Brisk Tide Logo. White base Can with mainly soft pink. I have mocked one up with Brisk Tide Logo in the middle similar to the Body Spray cans. Good Luck.
Target Market(s)
Females
Industry/Entity Type
Grocery
Colors
ffffff
e34197
e667a6
eea4c8
f9d9e8
Requirements
Must have
- White Can base with Pink colour tones
Nice to have
- Modern fresh feel
Should not have
- No dark colours soft pinks

```html
<!DOCTYPE html>
<html lang="en">
<head>
<meta charset="utf-8">
<title>Brisk Tide Sensitive Shaving Foam – Can Label</title>
<link rel="stylesheet" href="https://fonts.googleapis.com/css2?family=Montserrat:wght@400;600;800&family=Open+Sans:wght@400;700&display=swap">
<style>
  :root {
    --white: #ffffff;
    --magenta: #e34197;
    --pink-mid: #e667a6;
    --pink-soft: #eea4c8;
    --pink-pale: #f9d9e8;
    --plum-text: #8a1457;
    --backdrop: #545456;
  }
  * { box-sizing: border-box; margin: 0; padding: 0; }
  html, body { width: 1200px; height: 782px; overflow: hidden; }
  body { background: var(--backdrop); font-family: "Open Sans", Arial, sans-serif; }

  .canvas { position: relative; width: 1200px; height: 782px; }

  .label {
    position: absolute; left: 315px; top: 28px;
    width: 570px; height: 725px; overflow: hidden;
    background: linear-gradient(160deg, var(--pink-pale) 0%, #f6c7dd 55%, var(--pink-soft) 100%);
  }
  .label-curves { position: absolute; inset: 0; }

  .brand-line {
    position: absolute; left: 0; top: 151px; width: 322px; height: 3px;
    background: var(--magenta);
  }
  .brand-name {
    position: absolute; font-family: "Montserrat", Arial, sans-serif;
    font-weight: 800; color: var(--magenta); text-transform: uppercase;
    letter-spacing: 0.5px; white-space: nowrap; line-height: 1;
  }
  .brand-name--main { left: 42px; top: 92px; font-size: 32px; }
  .brand-name--panel { left: 357px; top: 44px; font-size: 22px; }
  .brand-name--small { left: 342px; top: 474px; font-size: 14px; }

  .range-pill {
    position: absolute; background: var(--magenta); color: var(--white);
    font-family: "Montserrat", Arial, sans-serif; font-weight: 600;
    text-transform: uppercase; text-align: center; border-radius: 6px;
    border: 2px solid rgba(255,255,255,.6); white-space: nowrap;
  }
  .range-pill--main { left: 60px; top: 142px; width: 162px; height: 24px; font-size: 14px; line-height: 20px; letter-spacing: 2.5px; }
  .range-pill--panel { left: 340px; top: 81px; width: 177px; height: 19px; font-size: 12px; line-height: 15px; letter-spacing: 3px; }

  .hero-photo {
    position: absolute; left: 39px; top: 215px; width: 220px; height: 220px; border-radius: 50%;
    background: radial-gradient(circle at 40% 40%, #fdeef5 0%, #f3c2da 60%, #eaa6c8 100%);
    border: 2px solid rgba(255,255,255,.7);
  }
  .foam-area {
    position: absolute; border-radius: 6px;
    background: linear-gradient(180deg, #ffffff 0%, #f6e6ee 100%);
  }
  .foam-area--hero { left: 74px; top: 487px; width: 135px; height: 110px; }
  .foam-area--panel { left: 440px; top: 430px; width: 77px; height: 62px; }

  .product-title {
    position: absolute; left: 60px; top: 614px; color: var(--white);
    font-family: "Montserrat", Arial, sans-serif; font-weight: 600; text-transform: uppercase;
    text-shadow: 0 0 1px var(--pink-mid);
  }
  .product-title__line1 { display: block; font-size: 30px; line-height: 33px; }
  .product-title__line2 { display: block; font-size: 20px; line-height: 24px; }
  .product-volume {
    position: absolute; left: 101px; top: 675px; font-size: 14px;
    color: var(--magenta); font-family: "Open Sans", Arial, sans-serif;
  }

  .info-panel {
    position: absolute; left: 322px; top: 90px; width: 215px; height: 595px;
    background: rgba(249, 217, 232, .75); border-radius: 10px;
  }
  .info-copy {
    position: absolute; left: 340px; top: 112px; width: 186px;
    font-size: 7.6px; line-height: 10.4px; color: var(--plum-text);
  }
  .info-copy p { margin-bottom: 10px; }
  .info-copy strong { display: block; font-weight: 700; }
  .info-copy--small { top: 500px; }

  .icon-grid {
    position: absolute; left: 339px; top: 553px; width: 128px;
    display: grid; grid-template-columns: repeat(3, 34px); gap: 4px 11px;
  }
  .icon-badge {
    width: 34px; height: 34px; border-radius: 50%; background: var(--pink-soft);
    color: var(--white); font-size: 6px; text-align: center; line-height: 34px;
  }
  .panel-volume {
    position: absolute; left: 340px; top: 640px; color: var(--white);
    font-size: 15px; line-height: 20px;
  }
</style>
</head>
<body>
<main class="canvas">
  <section class="label">
    <svg class="label-curves" width="570" height="725" viewBox="0 0 570 725" aria-hidden="true">
      <path d="M0 300 C 120 380, 200 560, 570 520" fill="none" stroke="#ffffff" stroke-opacity=".35" stroke-width="40"/>
      <path d="M0 620 C 160 560, 300 640, 570 600" fill="none" stroke="#ffffff" stroke-opacity=".25" stroke-width="24"/>
      <path d="M120 0 C 200 120, 300 160, 570 140" fill="none" stroke="#ffffff" stroke-opacity=".3" stroke-width="18"/>
    </svg>

    <div class="brand-line"></div>
    <div class="brand-name brand-name--main">Brisk Tide</div>
    <div class="range-pill range-pill--main">Soft Petal</div>

    <div class="hero-photo" role="img" aria-label="Photo of smooth crossed legs in a soft pink circle with bubbles"></div>
    <div class="foam-area foam-area--hero" role="img" aria-label="Illustration of a white shaving foam swirl"></div>

    <h1 class="product-title">
      <span class="product-title__line1">Sensitive</span>
      <span class="product-title__line2">Shaving Foam</span>
    </h1>
    <div class="product-volume">200ml - 100g</div>

    <div class="info-panel"></div>
    <div class="brand-name brand-name--panel">Brisk Tide</div>
    <div class="range-pill range-pill--panel">Soft Petal</div>

    <div class="info-copy">
      <p>Lorem ipsum dolor sit amet, consectetur adipiscing elit. Maecenas vitae tortor sit amet est pulvinar pharetra.<br>Donec non eros facilisis, elementum neque vel, hendrerit lectus. Nam placerat augue non magna porta iaculis.<br>Phasellus pretium porta libero, a rutrum ipsum. Duis blandit dignissim leo id eleifend. Vestibulum tincidunt enim fermentum justo mollis dapibus.</p>
      <p><strong>Sed ut dapibus quam.</strong>Mauris felis eros, rhoncus ut venenatis quis, blandit pulvinar metus.</p>
      <p><strong>Praesent magna nisi</strong>Praesent magna nisi, imperdiet vel felis egestas, ultrices dictum dui.</p>
      <p><strong>Quisque eget sem enim.</strong>Quisque eget sem enim. Sed molestie turpis et iaculis consequat.</p>
      <p><strong>Suspendisse</strong>Suspendisse sed augue bibendum, finibus lacus non, viverra dolor.</p>
      <p><strong>Duis placerat</strong>Duis placerat sodales mollis. Etiam in mattis velit, id rhoncus quam.</p>
    </div>

    <div class="foam-area foam-area--panel" role="img" aria-label="Small illustration of a white shaving foam swirl"></div>
    <div class="brand-name brand-name--small">Brisk Tide</div>
    <div class="info-copy info-copy--small">
      <p>Lorem ipsum dolor sit amet, consectetuer adipiscing elit, sed diam nonummy nibh euismod tincidunt. laoreet dolore magna aliquam erat volutpat</p>
    </div>

    <div class="icon-grid">
      <div class="icon-badge">ICON</div>
      <div class="icon-badge">ICON</div>
      <div class="icon-badge">ICON</div>
      <div class="icon-badge">ICON</div>
      <div class="icon-badge">ICON</div>
      <div class="icon-badge">ICON</div>
    </div>

    <div class="panel-volume">200ml<br>100g</div>
  </section>
</main>
</body>
</html>
```